Design of a carbonated cola drink

our competitor is selling brindle cola
their design is en closed
we need a similar design colours but we cant use
brindle cola
we were thinking of usuing
the words KVO cola
using a bit of the american flag colors red and blue
designs for three flavors shown below should be shown
the main drink colour is zapp red
orange bluma orange
punch like wintzel /zolvin burst

Target Market(s)

pacific islands

Requirements
Must have
• mentioned above
Nice to have
• mentioned above

```html
<!DOCTYPE html>
<html lang="en">
<head>
<meta charset="utf-8">
<title>KVO Cola – Can Label Variations</title>
<link rel="stylesheet" href="https://fonts.googleapis.com/css2?family=Playfair+Display:ital,wght@0,700;1,700&display=swap">
<style>
  :root {
    --bg: #ffffff;
    --red-light: #c8202a;
    --red-mid: #a3151c;
    --red-dark: #5a0a0e;
    --band: #c0393f;
    --band-edge: #e6c9ca;
    --ink: #fbf7f2;
  }
  html, body {
    margin: 0;
    padding: 0;
    width: 1200px;
    height: 1200px;
    overflow: hidden;
    background: var(--bg);
  }
  .canvas {
    position: relative;
    width: 1200px;
    height: 1200px;
  }
  .label {
    position: absolute;
    top: 276px;
    width: 208px;
    height: 560px;
  }
  .label--one { left: 78px; }
  .label--two { left: 356px; }
  .label--three { left: 634px; }
  .label--four { left: 930px; }
  .label-top {
    font-family: "Playfair Display", serif;
    font-weight: 700;
    font-style: italic;
    font-size: 13px;
    fill: var(--ink);
    letter-spacing: 0.5px;
  }
  .wordmark {
    font-family: "Playfair Display", serif;
    font-weight: 700;
    fill: var(--ink);
  }
</style>
</head>
<body>
<main class="canvas">
  <svg width="0" height="0" aria-hidden="true" style="position:absolute">
    <defs>
      <linearGradient id="can-body" x1="0" y1="0" x2="1" y2="0">
        <stop offset="0" stop-color="var(--red-mid)"/>
        <stop offset="0.3" stop-color="var(--red-light)"/>
        <stop offset="0.75" stop-color="var(--red-mid)"/>
        <stop offset="1" stop-color="var(--red-dark)"/>
      </linearGradient>
      <linearGradient id="can-shade" x1="0" y1="0" x2="0" y2="1">
        <stop offset="0" stop-color="#000" stop-opacity="0"/>
        <stop offset="0.55" stop-color="#000" stop-opacity="0.25"/>
        <stop offset="1" stop-color="#000" stop-opacity="0"/>
      </linearGradient>
    </defs>
  </svg>

  <!-- Variation 1 -->
  <svg class="label label--one" viewBox="0 0 208 560">
    <rect class="label-body" width="208" height="560" rx="6" fill="url(#can-body)"/>
    <rect width="208" height="560" rx="6" fill="url(#can-shade)"/>
    <text class="label-top" x="104" y="24" text-anchor="middle">KVO COLA</text>
    <polygon class="label-band" points="0,120 208,36 208,74 0,158" fill="var(--band)" stroke="var(--band-edge)" stroke-width="2"/>
    <polygon class="label-band" points="0,510 208,430 208,468 0,548" fill="var(--band)" stroke="var(--band-edge)" stroke-width="2"/>
    <circle cx="150" cy="192" r="22" fill="var(--ink)"/>
    <text class="wordmark" font-size="74" transform="translate(112 420) rotate(-72)">KVO</text>
    <text class="wordmark" font-size="50" transform="translate(166 440) rotate(-72)">cola</text>
  </svg>

  <!-- Variation 2 -->
  <svg class="label label--two" viewBox="0 0 208 560">
    <rect width="208" height="560" rx="6" fill="url(#can-body)"/>
    <rect width="208" height="560" rx="6" fill="url(#can-shade)"/>
    <text class="label-top" x="104" y="24" text-anchor="middle">KVO COLA</text>
    <polygon points="0,120 208,36 208,74 0,158" fill="var(--band)" stroke="var(--band-edge)" stroke-width="2"/>
    <polygon points="0,510 208,430 208,468 0,548" fill="var(--band)" stroke="var(--band-edge)" stroke-width="2"/>
    <circle cx="134" cy="192" r="22" fill="var(--ink)"/>
    <text class="wordmark" font-size="70" transform="translate(106 420) rotate(-70)">KVO</text>
    <text class="wordmark" font-size="50" transform="translate(160 440) rotate(-70)">cola</text>
  </svg>

  <!-- Variation 3 -->
  <svg class="label label--three" viewBox="0 0 208 560">
    <rect width="208" height="560" rx="6" fill="url(#can-body)"/>
    <rect width="208" height="560" rx="6" fill="url(#can-shade)"/>
    <text class="label-top" x="104" y="24" text-anchor="middle">KVO COLA</text>
    <polygon points="0,120 208,36 208,74 0,158" fill="var(--band)" stroke="var(--band-edge)" stroke-width="2"/>
    <polygon points="0,510 208,430 208,468 0,548" fill="var(--band)" stroke="var(--band-edge)" stroke-width="2"/>
    <circle cx="130" cy="192" r="22" fill="var(--ink)"/>
    <text class="wordmark" font-size="76" transform="translate(98 410) rotate(-66)">KVO</text>
    <text class="wordmark" font-size="50" transform="translate(160 428) rotate(-66)">cola</text>
  </svg>

  <!-- Variation 4 -->
  <svg class="label label--four" viewBox="0 0 208 560">
    <rect width="208" height="560" rx="6" fill="url(#can-body)"/>
    <rect width="208" height="560" rx="6" fill="url(#can-shade)"/>
    <text class="label-top" x="104" y="24" text-anchor="middle">KVO COLA</text>
    <polygon points="0,120 208,36 208,74 0,158" fill="var(--band)" stroke="var(--band-edge)" stroke-width="2"/>
    <polygon points="0,510 208,430 208,468 0,548" fill="var(--band)" stroke="var(--band-edge)" stroke-width="2"/>
    <circle cx="122" cy="192" r="22" fill="var(--ink)"/>
    <text class="wordmark" font-size="74" transform="translate(100 424) rotate(-76)">KVO</text>
    <text class="wordmark" font-size="50" transform="translate(158 440) rotate(-76)">cola</text>
  </svg>
</main>
</body>
</html>
```